Locksmith Business Cards

My father-in-law is in need of new business cards for his locksmith business and I need to impress him. Kindly help me out!

You can see the previous business card attached. It is a family run business in North Wales.

No individual names on the cards.

Key Things to Feature:
- The words "Prompt", "Local", "Reliable" (as you can see under the logo on the website)
- 24h Emergency Service
- Covering All of North Wales, the Wirral and Chester
- The color blue
- A key or a lock would be interesting (similar to the ones that come up when you google locksmith business card)

Optional (only if design includes bullet points, like the example below):
https://imgvaultcdnx.net/design_img/318264/57190/57190_2749031_318264_image.jpg
- Residential / Commercial / Automotive
- Alarms & Cameras
- Key Cutting & Safes

https://www.bryncoed-locksmiths-demo.co.uk/

Locksmith

01632 960 418
07700 900 362
bryncoedlocksmiths@mailvalex.com
Bryncoed Locksmiths, Hafod Barn, 4 Pennant Rd., Llandudno LL39 7QZ
www.bryncoed-locksmiths-demo.co.uk

• - The words "Prompt", "Local", "Reliable" (as you can see under the logo on the website)
• - 24h Emergency Service
• - Covering All of North Wales, the Wirral and Chester
• - A key or a lock would be interesting (similar to the ones that come up when you google locksmith business card)

```html
<!DOCTYPE html>
<html lang="en">
<head>
<meta charset="utf-8">
<title>Bryncoed Locksmiths – Business Card</title>
<link rel="stylesheet" href="https://fonts.googleapis.com/css2?family=Arimo:wght@400;700&display=swap">
<style>
  :root {
    --card-bg: #10141c;
    --ink: #ffffff;
    --brand-blue: #1a5cff;
    --muted: #9fb4e8;
  }
  html, body {
    margin: 0;
    padding: 0;
    width: 1200px;
    height: 678px;
    overflow: hidden;
    background: var(--card-bg);
  }
  .card {
    position: relative;
    width: 1200px;
    height: 678px;
    background: var(--card-bg);
    color: var(--ink);
    font-family: "Arimo", Arial, sans-serif;
    font-weight: 700;
  }
  .tagline {
    position: absolute;
    left: 81px;
    top: 74px;
    margin: 0;
    font-size: 38px;
    line-height: 1;
    letter-spacing: 4px;
  }
  .contact-list {
    position: absolute;
    left: 82px;
    top: 254px;
    margin: 0;
    padding: 0;
    list-style: none;
    font-size: 29px;
    line-height: 1;
    letter-spacing: 3.6px;
  }
  .contact-list li {
    height: 61.8px;
  }
  .brand {
    position: absolute;
    left: 820px;
    top: 80px;
    display: flex;
    align-items: center;
    gap: 22px;
  }
  .brand-dot {
    width: 86px;
    height: 86px;
    border-radius: 50%;
    background: var(--brand-blue);
    flex: none;
  }
  .brand-name {
    margin: 0;
    font-size: 34px;
    line-height: 1.15;
    letter-spacing: 1px;
    color: var(--ink);
  }
  .values {
    position: absolute;
    left: 820px;
    top: 186px;
    margin: 0;
    font-size: 19px;
    line-height: 1;
    letter-spacing: 3px;
    color: var(--brand-blue);
  }
  .emergency {
    position: absolute;
    left: 820px;
    top: 262px;
    display: flex;
    align-items: center;
    gap: 18px;
  }
  .emergency-icon {
    width: 54px;
    height: 64px;
    flex: none;
  }
  .emergency-text {
    margin: 0;
    font-size: 26px;
    line-height: 1.2;
    letter-spacing: 2px;
  }
  .emergency-text .accent {
    color: var(--brand-blue);
  }
  .coverage {
    position: absolute;
    left: 82px;
    right: 82px;
    top: 622px;
    margin: 0;
    padding-top: 14px;
    border-top: 2px solid var(--brand-blue);
    font-size: 20px;
    font-weight: 400;
    line-height: 1;
    letter-spacing: 2.4px;
    color: var(--muted);
  }
</style>
</head>
<body>
  <main class="card">
    <p class="tagline">PRIVATE AND COMMERCIAL</p>

    <div class="brand">
      <span class="brand-dot" aria-hidden="true"></span>
      <p class="brand-name">BRYNCOED<br>LOCKSMITHS</p>
    </div>

    <p class="values">PROMPT &#8226; LOCAL &#8226; RELIABLE</p>

    <div class="emergency">
      <svg class="emergency-icon" viewBox="0 0 54 64" aria-hidden="true">
        <path d="M14 28 V18 a13 13 0 0 1 26 0 V28" fill="none" stroke="#1a5cff" stroke-width="5"/>
        <rect x="4" y="28" width="46" height="33" rx="5" fill="none" stroke="#1a5cff" stroke-width="5"/>
        <line x1="27" y1="39" x2="27" y2="50" stroke="#ffffff" stroke-width="5" stroke-linecap="round"/>
      </svg>
      <p class="emergency-text"><span class="accent">24H</span> EMERGENCY<br>SERVICE</p>
    </div>

    <ul class="contact-list">
      <li class="contact-phone">01632 960 418</li>
      <li class="contact-mobile">07700 900 362</li>
      <li class="contact-email">bryncoedlocksmiths@mailvalex.com</li>
      <li class="contact-company">Bryncoed Locksmiths,</li>
      <li class="contact-address">Hafod Barn, 4 Pennant Rd., Llandudno LL39 7QZ</li>
      <li class="contact-web">www.bryncoed-locksmiths-demo.co.uk</li>
    </ul>

    <p class="coverage">Covering All of North Wales, the Wirral and Chester</p>
  </main>
</body>
</html>
```